Meridale Dental Business Card

Please design a professional but colorful looking business card. Our new logo is attached. The card also needs the following information:
For ALL Your Dental Needs
Curtis L. Hobbel, D.D.S.
918-555-0147
20463-C North Fernwick, Wrenfield, KS 74031
www.meridaledentalok.example

Industry/Entity Type

Business

Colors

Designer to choose colors to be used in the design.

```html
<!DOCTYPE html>
<html lang="en">
<head>
<meta charset="UTF-8">
<title>Meridale Dental Business Card</title>
<link rel="stylesheet" href="https://fonts.googleapis.com/css2?family=Archivo+Black&family=Questrial&display=swap">
<style>
  :root {
    --page-bg: #e9e6e1;
    --card-light: #f4fbff;
    --card-mid: #b9e3f6;
    --card-edge: #5fc1ea;
    --band-top: #1f8fd4;
    --band-bottom: #0b63b4;
    --band-strip: #0a57a6;
    --headline: #ffe81f;
    --contact: #ffffff;
    --brand: #3d4a57;
    --brand-mark: #2f8fd0;
    --tagline: #5a6672;
  }
  * { margin: 0; padding: 0; box-sizing: border-box; }
  html, body {
    width: 1200px;
    height: 1023px;
    overflow: hidden;
    background: var(--page-bg);
  }
  .stage {
    width: 1200px;
    height: 1023px;
    display: flex;
    align-items: center;
    justify-content: center;
  }
  .business-card {
    position: relative;
    width: 900px;
    height: 514px;
    border-radius: 6px;
    overflow: hidden;
    background:
      radial-gradient(ellipse 70% 80% at 45% 35%, var(--card-light) 0%, var(--card-mid) 60%, var(--card-edge) 100%);
    box-shadow: 0 10px 30px rgba(0, 0, 0, 0.18);
    font-family: "Questrial", sans-serif;
  }
  .brand {
    position: absolute;
    top: 118px;
    left: 0;
    right: 0;
    display: flex;
    flex-direction: column;
    align-items: center;
    gap: 14px;
  }
  .brand-lockup {
    display: flex;
    align-items: center;
    gap: 20px;
  }
  .brand-mark {
    width: 46px;
    height: 46px;
    background: var(--brand-mark);
  }
  .brand-name {
    font-family: "Questrial", sans-serif;
    font-size: 58px;
    letter-spacing: 3px;
    text-transform: uppercase;
    color: var(--brand);
  }
  .brand-tagline {
    font-size: 15px;
    letter-spacing: 2px;
    text-transform: uppercase;
    color: var(--tagline);
  }
  .info-band {
    position: absolute;
    left: 0;
    right: 0;
    bottom: 0;
    height: 184px;
    background: linear-gradient(180deg, var(--band-top) 0%, var(--band-bottom) 100%);
    padding: 22px 48px 0 72px;
  }
  .info-band::after {
    content: "";
    position: absolute;
    left: 0;
    right: 0;
    bottom: 0;
    height: 14px;
    background: var(--band-strip);
  }
  .headline {
    font-family: "Archivo Black", sans-serif;
    font-size: 40px;
    color: var(--headline);
    letter-spacing: 0.5px;
    line-height: 1;
  }
  .contact-row {
    display: flex;
    align-items: stretch;
    margin-top: 22px;
    color: var(--contact);
    font-size: 21px;
    line-height: 1.45;
  }
  .contact-person { padding-right: 26px; }
  .contact-divider {
    width: 2px;
    background: var(--contact);
    margin: 4px 0;
  }
  .contact-office { padding-left: 26px; }
</style>
</head>
<body>
  <main class="stage">
    <article class="business-card">
      <header class="brand">
        <div class="brand-lockup">
          <span class="brand-mark" aria-hidden="true"></span>
          <span class="brand-name">Meridale Dental</span>
        </div>
        <p class="brand-tagline">Gentle Modern Dentistry, Family Care</p>
      </header>
      <section class="info-band">
        <h1 class="headline">For ALL Your Dental Needs</h1>
        <div class="contact-row">
          <div class="contact-person">
            <p class="contact-name">Curtis L. Hobbel, D.D.S.</p>
            <p class="contact-phone">918-555-0147</p>
          </div>
          <span class="contact-divider" aria-hidden="true"></span>
          <div class="contact-office">
            <p class="contact-address">20463-C North Fernwick, Wrenfield, KS 74031</p>
            <p class="contact-web">www.meridaledentalok.example</p>
          </div>
        </div>
      </section>
    </article>
  </main>
</body>
</html>
```